Email Sig, Letterhead, Business Card Design

Need a stationary package including email signature, letterhead/envelope, and business card design incorporating our new logo.

```html
<!DOCTYPE html>
<html lang="en">
<head>
<meta charset="utf-8">
<title>Corbin Engineering Stationery</title>
<link href="https://fonts.googleapis.com/css2?family=Open+Sans:wght@400;600&family=Roboto:wght@300&family=Cinzel:wght@400&family=Great+Vibes&display=swap" rel="stylesheet">
<style>
:root{
  --bg:#a7a8ac;
  --paper:#ffffff;
  --blue:#1a64a0;
  --orange:#f05a22;
  --ink:#333333;
  --muted:#555a60;
  --faint:#eceef1;
}
*{margin:0;padding:0;box-sizing:border-box}
html,body{width:1200px;height:857px;overflow:hidden;background:var(--bg)}
body{position:relative;font-family:"Open Sans",sans-serif;color:var(--ink)}
.piece{position:absolute;background:var(--paper);overflow:hidden}
.abs{position:absolute}
.brand{position:absolute;text-align:center;white-space:nowrap}
.brand-mark{display:block;margin:0 auto;border-radius:50%;background:var(--blue)}
.brand-name{display:block;font-family:"Open Sans",sans-serif;font-weight:600;color:var(--orange);line-height:1}
.brand-sub{display:block;font-family:"Open Sans",sans-serif;font-weight:600;color:var(--blue);line-height:1.2;letter-spacing:.02em}
.band{position:absolute;left:0;right:0;background:var(--blue)}
.band-accent{position:absolute;top:0;right:0;bottom:0;background:var(--orange)}
.band-dot{position:absolute;border-radius:50%;background:var(--paper);border:1px solid var(--blue)}
.band-text{position:absolute;color:#fff;white-space:nowrap;font-family:"Open Sans",sans-serif}
.contact{position:absolute;font-family:"Open Sans",sans-serif;color:var(--muted);white-space:nowrap}
.contact li{list-style:none;display:flex;align-items:center}
.contact svg{flex:none;margin-right:.45em}
.divider{position:absolute;width:1px;background:#999}
.faint-shape{position:absolute;border-radius:50%;background:radial-gradient(circle,#f1f2f4 0%,#f6f7f8 60%,rgba(255,255,255,0) 72%)}

/* letterhead */
.letterhead{left:274px;top:146px;width:400px;height:566px}
.letter{position:absolute;left:42px;top:133px;width:315px;font-family:"Roboto",sans-serif;font-weight:300;font-size:6.9px;line-height:9.4px;color:var(--ink)}
.letter p{text-align:justify;margin-bottom:9.4px}
.letter .date{margin-bottom:9.4px}
.letter .recipient{margin-bottom:18.8px}
.signoff{position:absolute;left:42px;top:425px;font-family:"Roboto",sans-serif;font-weight:300;font-size:6.9px;color:var(--ink)}
.signature{position:absolute;left:42px;top:436px;font-family:"Great Vibes",cursive;font-size:15px;color:#222}

/* email signature */
.email-sig{left:699px;top:163px;width:360px;height:116px}
.sig-name{position:absolute;left:146px;top:21px;font-family:"Cinzel",serif;font-size:9.5px;color:var(--orange);letter-spacing:.04em;white-space:nowrap}
.sig-title{position:absolute;left:146px;top:31px;font-size:7px;color:var(--muted)}
.social{position:absolute;left:282px;top:23px;display:flex;gap:2px}
.social span{width:9.5px;height:9.5px;border-radius:50%;background:var(--orange)}

/* envelope */
.envelope-front{left:699px;top:303px;width:439px;height:191px}
.envelope-back{left:699px;top:520px;width:439px;height:191px}
.flap-name{position:absolute;left:0;right:0;top:19px;text-align:center}

/* business cards */
.card-front{left:62px;top:472px;width:187px;height:107px}
.card-back{left:62px;top:605px;width:187px;height:107px;background:var(--blue)}
.card-name{position:absolute;left:100px;top:35px;font-size:5.5px;font-weight:600;color:var(--orange);white-space:nowrap}
.card-title{position:absolute;left:100px;top:42px;font-size:3.8px;color:var(--blue)}
.card-web{position:absolute;left:0;right:0;top:91px;text-align:center;font-size:4px;color:#fff}
</style>
</head>
<body>

<!-- Business card front -->
<section class="piece card-front" aria-label="Business card front">
  <div class="brand" style="left:23px;top:34px;width:68px">
    <span class="brand-mark" style="width:20px;height:20px"></span>
    <span class="brand-name" style="font-size:6px;margin-top:4px">CORBIN ENGINEERING</span>
    <span class="brand-sub" style="font-size:2px">4120 CEDAR RIDGE LANE, ELMWOOD, TEXAS 77410</span>
    <span class="brand-sub" style="font-size:1.6px;color:var(--orange)">TBPE FIRM REGISTRATION F-1234</span>
  </div>
  <div class="divider" style="left:94px;top:36px;height:34px"></div>
  <div class="card-name">Daniel Hart</div>
  <div class="card-title">Founder</div>
  <ul class="contact" style="left:100px;top:53px;font-size:3.6px;line-height:5.4px">
    <li><svg width="3" height="3" viewBox="0 0 10 10"><path d="M2 1l2 0 1 2.5-1.3 1a6 6 0 0 0 2.8 2.8l1-1.3L10 7v2a1 1 0 0 1-1 1A9 9 0 0 1 0 1a1 1 0 0 1 1-1z" fill="var(--orange)"/></svg>(+1) 555.010.4200</li>
    <li><svg width="3" height="3" viewBox="0 0 10 10"><rect x=".5" y="2" width="9" height="6" fill="none" stroke="var(--orange)"/><path d="M.5 2l4.5 3.5L9.5 2" fill="none" stroke="var(--orange)"/></svg>info@corbin-engineering.com</li>
    <li><svg width="3" height="3" viewBox="0 0 10 10"><circle cx="5" cy="5" r="4.5" fill="var(--orange)"/></svg>www.corbin-engineering.com</li>
  </ul>
  <div class="band" style="top:89px;height:8px">
    <div class="band-accent" style="width:6px"></div>
    <span class="band-text" style="left:8px;top:1.6px;font-size:4px">Corbin Engineering Limited, 4120 Cedar Ridge Lane, Elmwood, Texas 77410</span>
  </div>
  <span class="band-dot" style="left:170px;top:86px;width:12px;height:12px"></span>
</section>

<!-- Business card back -->
<section class="piece card-back" aria-label="Business card back">
  <div class="faint-shape" role="img" aria-label="Faint enlarged brand symbol" style="left:120px;top:-10px;width:110px;height:120px;background:radial-gradient(circle,#2a70aa 0%,#2169a4 55%,rgba(26,100,160,0) 72%)"></div>
  <div class="brand" style="left:50px;top:26px;width:86px">
    <span class="brand-mark" style="width:28px;height:28px;background:#fff"></span>
    <span class="brand-name" style="font-size:8.5px;margin-top:6px;color:#fff">CORBIN ENGINEERING</span>
    <span class="brand-sub" style="font-size:2.4px;color:#fff">4120 CEDAR RIDGE LANE, ELMWOOD, TEXAS 77410</span>
    <span class="brand-sub" style="font-size:2px;color:#fff">TBPE FIRM REGISTRATION F-1234</span>
  </div>
  <div class="card-web">www.corbin-engineering.com</div>
</section>

<!-- Letterhead -->
<section class="piece letterhead" aria-label="Letterhead">
  <div class="faint-shape" role="img" aria-label="Faint enlarged brand symbol" style="left:-10px;top:395px;width:160px;height:170px"></div>
  <div class="brand" style="left:30px;top:13px;width:98px">
    <span class="brand-mark" style="width:30px;height:30px"></span>
    <span class="brand-name" style="font-size:9.8px;margin-top:8px">CORBIN ENGINEERING</span>
    <span class="brand-sub" style="font-size:2.6px">4120 CEDAR RIDGE LANE, ELMWOOD, TEXAS 77410</span>
    <span class="brand-sub" style="font-size:2.2px;color:var(--orange)">TBPE FIRM REGISTRATION F-1234</span>
  </div>
  <div class="divider" style="left:264px;top:44px;height:25px"></div>
  <ul class="contact" style="left:273px;top:42px;font-size:6.8px;line-height:8.2px">
    <li><svg width="5" height="5" viewBox="0 0 10 10"><path d="M2 1l2 0 1 2.5-1.3 1a6 6 0 0 0 2.8 2.8l1-1.3L10 7v2a1 1 0 0 1-1 1A9 9 0 0 1 0 1a1 1 0 0 1 1-1z" fill="var(--orange)"/></svg>(+1) 555.010.4200</li>
    <li><svg width="5" height="5" viewBox="0 0 10 10"><rect x=".5" y="2" width="9" height="6" fill="none" stroke="var(--orange)"/><path d="M.5 2l4.5 3.5L9.5 2" fill="none" stroke="var(--orange)"/></svg>info@corbin-engineering.com</li>
    <li><svg width="5" height="5" viewBox="0 0 10 10"><circle cx="5" cy="5" r="4.5" fill="var(--orange)"/></svg>www.corbin-engineering.com</li>
  </ul>
  <div class="letter">
    <div class="date">01 January 2050</div>
    <div class="recipient">Company (Pvt) Ltd.<br>PO Box 3355 Mainville St<br>Sample City Country 3355</div>
    <p>Dear Paul Anders,</p>
    <p>Lorem ipsum dolor sit amet, consectetuer adipiscing elit, sed diam nonummy nibh euismod tincidunt ut laoreet dolore magna aliquam erat volutpat. Ut wisi enim ad minim veniam, quis nostrud exerci tation ullamcorper suscipit lobortis nisl ut aliquip ex ea commodo consequat. Duis dolore te feugait nulla facilisi. Nam liber tempor cum soluta nobis eleifend option congue nihil imperdiet doming id quod mazim placerat facer possim assum. Lorem ipsum dolor sit amet, consectetuer adipiscing elit, sed diam nonummy nibh euismod tincidunt ut laoreet dolore magna aliquam erat volutpat. Ut wisi enim ad minim veniam, quis nostrud exerci tation ullamcorper suscipit lobortis nisl ut aliquip ex ea commodo consequat.</p>
    <p>Consectetuer adipiscing elit, sed diam nonummy nibh euismod tincidunt ut laoreet dolore magna aliquam erat volutpat. Ut wisi enim ad minim veniam, quis nostrud exerci tation ullamcorper suscipit lobortis nisl ut aliquip ex ea commodo consequat. Consectetuer adipiscing elit, sed diam nonummy nibh euismod tincidunt ut laoreet dolore magna aliquam erat volutpat. Ut wisi enim ad minim veniam, quis nostrud exerci tation ullamcorper suscipit lobortis nisl ut aliquip ex ea commodo consequat.</p>
    <p>Consectetuer adipiscing elit, sed diam nonummy nibh euismod tincidunt ut laoreet dolore magna aliquam erat volutpat. Ut wisi enim ad minim veniam, quis nostrud exerci tation ullamcorper suscipit lobortis nisl ut aliquip ex ea commodo consequat. Consectetuer adipiscing elit, sed diam nonummy nibh euismod tincidunt ut laoreet dolore magna aliquam erat volutpat. Ut wisi enim ad minim veniam, quis nostrud exerci tation ullamcorper suscipit lobortis nisl ut aliquip ex ea commodo consequat.</p>
  </div>
  <div class="signoff">Sincerely Yours</div>
  <div class="signature">Thomas Reed</div>
  <div class="band" style="top:543px;height:16px">
    <div class="band-accent" style="width:30px"></div>
    <span class="band-text" style="left:35px;top:3px;font-size:7px">Corbin Engineering Limited, 4120 Cedar Ridge Lane, Elmwood, Texas 77410</span>
  </div>
  <span class="band-dot" style="left:345px;top:537px;width:24px;height:24px"></span>
</section>

<!-- Email signature -->
<section class="piece email-sig" aria-label="Email signature">
  <div class="brand" style="left:23px;top:20px;width:98px">
    <span class="brand-mark" style="width:30px;height:30px"></span>
    <span class="brand-name" style="font-size:9.8px;margin-top:8px">CORBIN ENGINEERING</span>
    <span class="brand-sub" style="font-size:2.6px">4120 CEDAR RIDGE LANE, ELMWOOD, TEXAS 77410</span>
    <span class="brand-sub" style="font-size:2.2px;color:var(--orange)">TBPE FIRM REGISTRATION F-1234</span>
  </div>
  <div class="divider" style="left:132px;top:20px;height:59px"></div>
  <div class="sig-name">DANIEL HART</div>
  <div class="sig-title">Founder</div>
  <div class="social" aria-label="Social links"><span></span><span></span><span></span><span></span></div>
  <ul class="contact" style="left:146px;top:50px;font-size:7px;line-height:8.4px">
    <li><svg width="5" height="5" viewBox="0 0 10 10"><path d="M2 1l2 0 1 2.5-1.3 1a6 6 0 0 0 2.8 2.8l1-1.3L10 7v2a1 1 0 0 1-1 1A9 9 0 0 1 0 1a1 1 0 0 1 1-1z" fill="var(--orange)"/></svg>(+1) 555.010.4200</li>
    <li><svg width="5" height="5" viewBox="0 0 10 10"><rect x=".5" y="2" width="9" height="6" fill="none" stroke="var(--orange)"/><path d="M.5 2l4.5 3.5L9.5 2" fill="none" stroke="var(--orange)"/></svg>info@corbin-engineering.com</li>
    <li><svg width="5" height="5" viewBox="0 0 10 10"><circle cx="5" cy="5" r="4.5" fill="var(--orange)"/></svg>www.corbin-engineering.com</li>
  </ul>
  <div class="band" style="top:91px;height:16px">
    <div class="band-accent" style="width:38px"></div>
    <span class="band-text" style="left:33px;top:3px;font-size:7px;font-weight:600">Corbin Engineering Limited, 4120 Cedar Ridge Lane, Elmwood, Texas 77410</span>
  </div>
  <span class="band-dot" style="left:304px;top:84px;width:24px;height:24px"></span>
</section>

<!-- Envelope front -->
<section class="piece envelope-front" aria-label="Envelope front">
  <div class="faint-shape" role="img" aria-label="Faint enlarged brand symbol" style="left:305px;top:-10px;width:160px;height:140px"></div>
  <div class="brand" style="left:20px;top:23px;width:98px">
    <span class="brand-mark" style="width:30px;height:30px"></span>
    <span class="brand-name" style="font-size:9.8px;margin-top:8px">CORBIN ENGINEERING</span>
    <span class="brand-sub" style="font-size:2.6px">4120 CEDAR RIDGE LANE, ELMWOOD, TEXAS 77410</span>
    <span class="brand-sub" style="font-size:2.2px;color:var(--orange)">TBPE FIRM REGISTRATION F-1234</span>
  </div>
  <ul class="contact" style="left:26px;top:132px;font-size:6.8px;line-height:8px">
    <li><svg width="5" height="5" viewBox="0 0 10 10"><path d="M2 1l2 0 1 2.5-1.3 1a6 6 0 0 0 2.8 2.8l1-1.3L10 7v2a1 1 0 0 1-1 1A9 9 0 0 1 0 1a1 1 0 0 1 1-1z" fill="var(--orange)"/></svg>(+1) 555.010.4200</li>
    <li><svg width="5" height="5" viewBox="0 0 10 10"><rect x=".5" y="2" width="9" height="6" fill="none" stroke="var(--orange)"/><path d="M.5 2l4.5 3.5L9.5 2" fill="none" stroke="var(--orange)"/></svg>info@corbin-engineering.com</li>
    <li><svg width="5" height="5" viewBox="0 0 10 10"><circle cx="5" cy="5" r="4.5" fill="var(--orange)"/></svg>www.corbin-engineering.com</li>
  </ul>
  <div class="band" style="top:165px;height:15px">
    <div class="band-accent" style="width:31px"></div>
    <span class="band-text" style="left:26px;top:3px;font-size:6.8px">Corbin Engineering Limited, 4120 Cedar Ridge Lane, Elmwood, Texas 77410</span>
  </div>
  <span class="band-dot" style="left:387px;top:159px;width:24px;height:24px"></span>
</section>

<!-- Envelope back -->
<section class="piece envelope-back" aria-label="Envelope back">
  <svg class="abs" style="left:0;top:0" width="439" height="191" viewBox="0 0 439 191">
    <path d="M8 56 L6 185 M431 56 L433 185" stroke="#e2e3e6" stroke-width="1" fill="none"/>
    <path d="M0 0 H439 L426 54 Q424 62 414 62 H25 Q15 62 13 54 Z" fill="var(--blue)"/>
  </svg>
  <div class="flap-name">
    <span class="brand-name" style="font-size:11.5px;color:#fff">CORBIN ENGINEERING</span>
    <span class="brand-sub" style="font-size:3px;color:#fff;margin-top:1px">4120 CEDAR RIDGE LANE, ELMWOOD, TEXAS 77410</span>
    <span class="brand-sub" style="font-size:2.6px;color:#fff">TBPE FIRM REGISTRATION F-1234</span>
  </div>
</section>

</body>
</html>
```